Business Card Design

I'm a commercial general contractor remodel offices, hotels, health clubs and stores mostly San Francisco and the peninsula
the file I down loaded is kind of what I want I like the I beam with my company name in it, that would be fine with me but if you have better Idea will look at it you never know, I'm decided to give in and change my company name to how every one knows me, I have been in business since 1991, I like the I beam logo I included one of my old card from my old company for reference for you.

Industry/Entity Type

Business

Contact Information for Business Card

BRAXO CONSTRUCTION (is my company name)
Wendell Trusk contractor, LIc 314827
4158 Garnet Row, Larkton, California 94012
mobile, (415) 555-0147
phone (650) 555-0182
Fax, (650) 555-0183
email, braxo@braxoconstruction.example

```html
<!DOCTYPE html>
<html lang="en">
<head>
<meta charset="utf-8">
<title>Braxo Construction – Business Card</title>
<link rel="stylesheet" href="https://fonts.googleapis.com/css2?family=Source+Sans+3:wght@400;600&display=swap">
<style>
  :root {
    --page-bg: #e9e7e3;
    --card-light: #f4f4f4;
    --card-mid: #c9cacb;
    --skyline: #b9bbbd;
    --band: #2b2c2e;
    --accent: #1e9be0;
    --ink: #4a4b4d;
    --ink-soft: #8a8c8e;
    --band-text: #c7c8ca;
  }
  * { box-sizing: border-box; margin: 0; padding: 0; }
  html, body {
    width: 1200px; height: 800px; overflow: hidden;
    background: var(--page-bg);
    font-family: "Source Sans 3", "Source Sans Pro", sans-serif;
  }
  .canvas {
    width: 1200px; height: 800px;
    display: flex; align-items: center; justify-content: center;
  }
  .card {
    position: relative;
    width: 1050px; height: 600px;
    background: radial-gradient(ellipse at 62% 28%, var(--card-light) 0%, #dfe0e1 45%, var(--card-mid) 100%);
    box-shadow: 0 10px 30px rgba(0,0,0,.18);
    overflow: hidden;
    color: var(--ink);
  }
  .skyline {
    position: absolute; left: 0; top: 40px;
    width: 100%; height: 190px;
    background: linear-gradient(to bottom, rgba(185,187,189,0) 0%, rgba(185,187,189,.45) 60%, var(--skyline) 100%);
  }
  .brand {
    position: absolute; left: 430px; top: 105px;
    display: flex; align-items: center; gap: 16px;
  }
  .brand-mark { width: 22px; height: 22px; background: var(--accent); }
  .brand-name {
    font-weight: 600; font-size: 44px; letter-spacing: 3px;
    color: var(--accent);
  }
  .licence {
    position: absolute; right: 40px; top: 160px;
    font-size: 24px; letter-spacing: 2px; color: var(--ink-soft);
  }
  .name-band {
    position: absolute; left: 0; top: 235px;
    width: 100%; height: 62px;
    background: var(--band);
    font-size: 33px; letter-spacing: 1px;
  }
  .name-band span {
    position: absolute; top: 0; line-height: 62px;
  }
  .name-band .person { left: 60px; color: var(--accent); }
  .name-band .role { left: 510px; color: var(--band-text); }
  .contact-list {
    position: absolute; list-style: none;
    font-size: 27px; line-height: 1;
  }
  .contact-list li {
    display: flex; align-items: center; gap: 22px;
    height: 54px;
  }
  .contact-list svg { width: 26px; height: 26px; flex: none; }
  .phones { left: 60px; top: 325px; }
  .details { left: 510px; top: 325px; }
  .details .address { align-items: flex-start; height: auto; padding: 12px 0; line-height: 1.25; }
  .details .address svg { margin-top: 4px; }
  .icon { fill: var(--accent); }
  .icon-line { fill: none; stroke: var(--accent); stroke-width: 2.4; }
</style>
</head>
<body>
<main class="canvas">
  <article class="card">
    <div class="skyline" role="img" aria-label="Faint grey silhouette of a suspension bridge and city skyline"></div>

    <div class="brand">
      <span class="brand-mark"></span>
      <span class="brand-name">BRAXO CONSTRUCTION</span>
    </div>

    <p class="licence">LIC 314827</p>

    <div class="name-band">
      <span class="person">WENDELL "BRAXO" TRUSK</span>
      <span class="role">CONTRACTOR</span>
    </div>

    <ul class="contact-list phones">
      <li>
        <svg viewBox="0 0 24 24" aria-label="Mobile"><rect class="icon" x="6" y="1" width="12" height="22" rx="2"/><rect x="8" y="4" width="8" height="13" fill="#fff"/><circle cx="12" cy="20" r="1.2" fill="#fff"/></svg>
        <span>(415) 555-0147</span>
      </li>
      <li>
        <svg viewBox="0 0 24 24" aria-label="Phone"><circle class="icon" cx="12" cy="12" r="11"/><path d="M8.5 6.5l2 2-1 1.5c.8 1.8 2.2 3.2 4 4l1.5-1 2 2-1.5 2c-4 0-8.5-4.5-8.5-8.5z" fill="#fff"/></svg>
        <span>(650) 555-0182</span>
      </li>
      <li>
        <svg viewBox="0 0 24 24" aria-label="Fax"><rect class="icon" x="2" y="3" width="20" height="19" rx="2"/><rect x="5" y="6" width="6" height="13" fill="#fff"/><rect x="13" y="6" width="6" height="4" fill="#fff"/><rect x="13" y="12" width="6" height="7" fill="#fff"/></svg>
        <span>(650) 555-0183</span>
      </li>
    </ul>

    <ul class="contact-list details">
      <li>
        <svg viewBox="0 0 24 24" aria-label="Email"><circle class="icon-line" cx="12" cy="12" r="10.5"/><rect class="icon" x="6" y="8" width="12" height="8" rx="1"/><path d="M6.5 8.5L12 13l5.5-4.5" fill="none" stroke="#fff" stroke-width="1.4"/></svg>
        <span>braxo@braxoconstruction.example</span>
      </li>
      <li class="address">
        <svg viewBox="0 0 24 24" aria-label="Address"><path class="icon" d="M12 1a8 8 0 0 0-8 8c0 6 8 14 8 14s8-8 8-14a8 8 0 0 0-8-8z"/><circle cx="12" cy="9" r="3" fill="#fff"/></svg>
        <span>4158 Garnet Row, Larkton<br>California 94012</span>
      </li>
      <li>
        <svg viewBox="0 0 24 24" aria-label="Website"><circle class="icon-line" cx="12" cy="12" r="10"/><ellipse class="icon-line" cx="12" cy="12" rx="4.5" ry="10"/><path class="icon-line" d="M2 12h20M4 6.5h16M4 17.5h16"/></svg>
        <span>www.braxoconstruction.example</span>
      </li>
    </ul>
  </article>
</main>
</body>
</html>
```